Need a business card for our overland brand!

We had the logo made and we need a great design for our business card. Use the logo provide or tweak it however you see fit.

Contact Information for Business Card

Name, Title, Telephone, email, website

```html
<!DOCTYPE html>
<html lang="en">
<head>
<meta charset="UTF-8">
<title>Northpass Overland – Business Card</title>
<link rel="stylesheet" href="https://fonts.googleapis.com/css2?family=Montserrat:wght@500;600;700&family=Roboto:wght@400&display=swap">
<style>
  :root {
    --navy: #1f3550;
    --navy-card: #1d3553;
    --navy-mark: #2c4a6e;
    --teal: #2aa3c6;
    --grey-text: #6a6f75;
    --white: #ffffff;
    --backdrop: #e6e7e9;
  }
  * { margin: 0; padding: 0; box-sizing: border-box; }
  html, body {
    width: 1200px;
    height: 1129px;
    overflow: hidden;
    background: var(--backdrop);
  }
  .canvas {
    position: relative;
    width: 1200px;
    height: 1129px;
  }
  .card {
    position: absolute;
    left: 220px;
    width: 760px;
    height: 434px;
    box-shadow: 0 6px 18px rgba(0,0,0,0.12);
  }
  .card--back {
    top: 95px;
    background: var(--navy-card);
    display: flex;
    align-items: center;
    justify-content: center;
  }
  .card--front {
    top: 600px;
    background: var(--white);
    display: flex;
    align-items: center;
  }
  .wordmark {
    font-family: "Montserrat", sans-serif;
    font-weight: 700;
    text-transform: uppercase;
    line-height: 0.95;
    text-align: center;
    letter-spacing: 1px;
  }
  .card--back .wordmark {
    color: var(--navy-mark);
    font-size: 64px;
  }
  .card--front .wordmark {
    color: var(--navy);
    font-size: 40px;
  }
  .front-brand {
    width: 330px;
    display: flex;
    justify-content: center;
    padding-left: 40px;
  }
  .divider {
    width: 1px;
    height: 230px;
    background: var(--navy);
    margin: 0 40px 0 30px;
  }
  .details { color: var(--grey-text); }
  .person-name {
    font-family: "Montserrat", sans-serif;
    font-weight: 600;
    font-size: 28px;
    color: var(--navy);
    letter-spacing: 0.5px;
  }
  .person-title {
    font-family: "Roboto", sans-serif;
    font-size: 23px;
    color: var(--teal);
    margin-top: 2px;
  }
  .contact-list {
    list-style: none;
    margin-top: 34px;
    font-family: "Roboto", sans-serif;
    font-size: 19px;
  }
  .contact-list li {
    display: flex;
    align-items: center;
    gap: 10px;
    margin-bottom: 6px;
  }
  .contact-icon {
    width: 20px;
    height: 20px;
    flex: none;
  }
</style>
</head>
<body>
<main class="canvas">
  <section class="card card--back" aria-label="Card back">
    <div class="wordmark">Northpass<br>Overland</div>
  </section>

  <section class="card card--front" aria-label="Card front">
    <div class="front-brand">
      <div class="wordmark">Northpass<br>Overland</div>
    </div>
    <div class="divider"></div>
    <div class="details">
      <div class="person-name">DALEN VARSK</div>
      <div class="person-title">Founder &amp; CEO</div>
      <ul class="contact-list">
        <li>
          <svg class="contact-icon" viewBox="0 0 24 24" aria-hidden="true"><path fill="#2aa3c6" d="M6.6 10.8a15.1 15.1 0 0 0 6.6 6.6l2.2-2.2c.3-.3.7-.4 1-.2 1.1.4 2.3.6 3.6.6.6 0 1 .4 1 1V20c0 .6-.4 1-1 1A17 17 0 0 1 3 4c0-.6.4-1 1-1h3.5c.6 0 1 .4 1 1 0 1.3.2 2.5.6 3.6.1.3 0 .7-.2 1z"/></svg>
          972-555-0148
        </li>
        <li>
          <svg class="contact-icon" viewBox="0 0 24 24" aria-hidden="true"><g fill="none" stroke="#2aa3c6" stroke-width="1.8"><rect x="2.5" y="5" width="19" height="14"/><path d="M2.5 5l9.5 8 9.5-8M2.5 19l7-6.5M21.5 19l-7-6.5"/></g></svg>
          info@northpassoverland.com
        </li>
        <li>
          <svg class="contact-icon" viewBox="0 0 24 24" aria-hidden="true"><g fill="none" stroke="#2aa3c6" stroke-width="1.6"><circle cx="12" cy="12" r="9.5"/><ellipse cx="12" cy="12" rx="4.5" ry="9.5"/><path d="M2.5 12h19M4 7h16M4 17h16"/></g></svg>
          www.northpassoverland.com
        </li>
      </ul>
    </div>
  </section>
</main>
</body>
</html>
```